A 'new law' boutique Australian law firm that provides specialist employment law and people managem

We value helping clients create results with respect workplaces. What differentiates us is we provide actionable training in understanding and dealing with people and ensure legal compliance fits with this approach. We would like a fresh approach to our training overview documents that we currently use in our current law firm (6 attached). Please use pictures, symbols etc consistent with our non-traditional law approach that captures the approach of each training session.. Attached is the logo and draft letterhead for Brook Legal which will launch soon.

Target Market(s)

HR Managers and in-house lawyers (non employment specialists) in mid-large Australian companies that are progressive with a relationship based approach to managing employee behaviours and disputes.

Industry/Entity Type

Human Resource

Font styles to use
Sans Serif

Colors
3176b5
33a6d7

Requirements
Must have
• 1 or 2 page PDF for each of the 6 documents that the wording supplied goes into your design which will be pretty similar as we want consistency with our documents

```html
<!DOCTYPE html>
<html lang="en">
<head>
<meta charset="utf-8">
<title>Contact Officer Training – Brook Legal</title>
<link href="https://fonts.googleapis.com/css2?family=Open+Sans:ital,wght@0,300;0,400;0,600;0,700;1,600&display=swap" rel="stylesheet">
<style>
  :root{
    --brand-blue:#3176b5;
    --brand-sky:#33a6d7;
    --sidebar:#2b6aa8;
    --sidebar-deep:#1f5189;
    --ink:#3d4650;
    --ink-soft:#5d6770;
    --band:#e3f0f8;
    --white:#ffffff;
  }
  *{box-sizing:border-box;margin:0;padding:0}
  html,body{width:849px;height:1200px;overflow:hidden;background:var(--white)}
  body{font-family:"Open Sans",Arial,sans-serif;color:var(--ink)}
  .sheet{position:relative;width:849px;height:1200px;overflow:hidden}

  /* left column */
  .main{position:absolute;left:0;top:0;width:660px;height:1200px}
  .brand{position:absolute;left:34px;top:40px;display:flex;align-items:center;gap:10px}
  .brand-mark{width:22px;height:22px;background:var(--brand-blue)}
  .brand-name{font-size:22px;font-weight:700;color:var(--brand-blue);letter-spacing:.5px}
  .contacts{position:absolute;left:498px;top:22px;list-style:none;font-size:10px;color:var(--ink-soft)}
  .contacts li{display:flex;align-items:center;gap:6px;height:18px}
  .contacts svg{width:11px;height:11px;fill:var(--brand-blue)}

  .title{position:absolute;left:250px;top:150px;width:390px;text-align:center;font-weight:300;color:var(--ink);line-height:1.1}
  .title span{display:block;font-size:40px}
  .section-label{position:absolute;right:24px;top:240px;font-size:18px;font-weight:600;color:var(--brand-blue)}

  .need-lead{position:absolute;left:50px;top:280px;width:590px;font-size:12px;line-height:1.55;color:var(--ink-soft);text-align:center}
  .need-visual{position:absolute;left:40px;top:420px;width:310px;height:200px;border-radius:6px;
    background:linear-gradient(160deg,#dfeef8 0%,#bcd9ee 55%,#eaf4fb 100%)}
  .need-text{position:absolute;left:375px;top:402px;width:265px;font-size:12px;line-height:1.55;color:var(--ink-soft);text-align:center}
  .need-text p{margin-bottom:12px}

  .outcomes-head{position:absolute;left:0;top:722px;width:660px;height:36px;background:var(--band);
    display:flex;align-items:center;padding-left:34px;font-size:17px;font-weight:700;color:var(--sidebar-deep)}
  .outcomes{position:absolute;left:34px;top:774px;width:590px;font-size:12px;line-height:1.6;color:var(--ink)}
  .outcomes .lead{font-weight:600;margin-bottom:8px}
  .outcomes ol{padding-left:18px}
  .outcomes li{margin-bottom:4px}

  /* right sidebar */
  .overview{position:absolute;left:660px;top:0;width:189px;height:1200px;background:var(--sidebar);color:var(--white);overflow:hidden}
  .overview h2{font-size:16px;font-weight:700;padding:40px 10px 8px}
  .topic h3{background:var(--brand-sky);font-size:12.5px;font-weight:700;padding:5px 10px;margin:8px 0 5px}
  .topic ul{list-style:none;padding:0 10px}
  .topic li{font-size:9.6px;line-height:1.34;padding-left:8px;position:relative;margin-bottom:3px}
  .topic li::before{content:"";position:absolute;left:0;top:5px;width:3px;height:3px;background:var(--white);border-radius:50%}
  .topic .example{font-weight:600;font-style:italic;padding-left:0}
  .topic .example::before{display:none}
</style>
</head>
<body>
<div class="sheet">
  <section class="main">
    <div class="brand">
      <span class="brand-mark"></span>
      <span class="brand-name">Brook Legal</span>
    </div>
    <ul class="contacts">
      <li><svg viewBox="0 0 12 12"><circle cx="6" cy="6" r="5.5"/></svg>www.brooklegal.com.au</li>
      <li><svg viewBox="0 0 12 12"><rect x="0.5" y="2" width="11" height="8"/></svg>hello@brooklegal.com.au</li>
      <li><svg viewBox="0 0 12 12"><path d="M3 1h2l1 3-1.5 1a6 6 0 0 0 2.5 2.5L8 6l3 1v2c0 1-1 2-2 2A8 8 0 0 1 1 3c0-1 1-2 2-2z"/></svg>+61 2 9000 0000</li>
    </ul>

    <h1 class="title"><span>Contact</span><span>Officer Training</span></h1>
    <div class="section-label">Training Need</div>

    <p class="need-lead">Unlawful or inappropriate behaviour in the workplace that is left unaddressed can impact on productivity and employee retention. Claims can be costly in terms of time and money as well as the impact on mental health from being involved in unresolved unfavourable behaviour.</p>
    <div class="need-visual" role="img" aria-label="Illustration of colleagues meeting around a table"></div>
    <div class="need-text">
      <p>Clear policies and procedures explaining the organisation's workplace behaviour expectations and how grievances will be managed are a minimum compliance requirement.</p>
      <p>The challenge is ensuring that employees understand the directions contained in those policies, what is unlawful and inappropriate behaviour and the options available to address those behaviours if they experience them or engage in them.</p>
      <p>Well trained Contact Officers provide another resource to assist the organisation to provide a safe and respectful workplace.</p>
    </div>

    <div class="outcomes-head">Learning Outcomes</div>
    <div class="outcomes">
      <p class="lead">Training will enable participants to perform their role of Contact Officer and to understand:</p>
      <ol>
        <li>The role and responsibilities of a Contact Officer</li>
        <li>What constitutes unlawful workplace behaviour.</li>
        <li>What is considered inappropriate behaviour in our workplace.</li>
        <li>How to apply understanding 'unlawful/inappropriate behaviour' to common scenarios.</li>
        <li>How to address and resolve grievances early.</li>
        <li>Options to resolve grievances internally and the Contact Officer role.</li>
        <li>External options and their pros and cons for resolving grievances.</li>
      </ol>
    </div>
  </section>

  <aside class="overview">
    <h2>Training Overview</h2>
    <div class="topic"><h3>Discrimination</h3><ul>
      <li>What is direct and indirect discrimination?</li>
      <li>What are the prescribed attributes?</li>
      <li>What are the exceptions to the general rules?</li>
      <li class="example">Practical examples of behaviour that may be discrimination</li></ul></div>
    <div class="topic"><h3>Harassment</h3><ul>
      <li>What is harassment?</li>
      <li>Are protected attributes relevant to harassment?</li>
      <li>What is the difference between harassment and sexual harassment?</li>
      <li>How does the reasonable person test work in relation to harassment?</li>
      <li class="example">Practical examples of behaviour that may be harassment or sexual harassment.</li></ul></div>
    <div class="topic"><h3>Bullying</h3><ul>
      <li>What is bullying?</li>
      <li>Explore how bullying differs to discrimination or inappropriate behaviour.</li>
      <li>Performance Management – when it will and will not be bullying.</li>
      <li>Is all workplace conflict bullying?</li>
      <li class="example">Practical examples of behaviour that may be bullying.</li></ul></div>
    <div class="topic"><h3>Victimisation &amp; Vilification</h3><ul>
      <li>What is Victimisation? What is Vilification?</li></ul></div>
    <div class="topic"><h3>Adverse Action</h3><ul>
      <li>What is adverse action and how does it differ to other unlawful behaviour?</li>
      <li>What is a workplace right?</li>
      <li>When is it lawful to terminate employment because of an employee's absence?</li>
      <li>How are the protected attributes relevant to adverse action?</li></ul></div>
    <div class="topic"><h3>The Contact Officer's role</h3><ul>
      <li>How to perform your role when approached by an employee – the 4 step approach. What not to do.</li>
      <li>What are the obligations with regard to Confidentiality?</li></ul></div>
    <div class="topic"><h3>Grievance Options</h3><ul>
      <li>Explain the options of complaint management – self management, informal internal management, formal internal management.</li>
      <li>How do they compare and what are the advantages and disadvantages of each approach, including seeking an apology?</li>
      <li>External options – advantages and disadvantages. Who decides which option?</li></ul></div>
    <div class="topic"><h3>Test Learning</h3><ul>
      <li>Real case group discussion.</li></ul></div>
  </aside>
</div>
</body>
</html>
```